Treppenlift Infoportal
Zielgruppe
Vermittlung von Aufzügen und Treppenliften.
Aufgabenstellung
Wir benötigen ein Design für ein Treppenlift-Portal.
Das Design sollte sehr anprechend & modern sein sowie möchlichst dazu führen, dass der Nutzer gerne seine Nutzerdaten in einem Formular eingibt, um nähere Informationen zu einem gewünschen Treppenlift zu erhalten.
Da die Seite ebenfalls sehr viele Informationen bereitstellt, ist es notwendig, eine horizontale Navigation mit einer ersten & zweiten Ebene zu integrieren.
Da die Interessentengruppe eher 50plus ist, wäre es schön, wenn bei der Designerstellung die Nutzerfreundlichkeit berücksichtigt werden würde.

```html
<!DOCTYPE html>
<html lang="de">
<head>
<meta charset="utf-8">
<title>Treppenlift Infoportal</title>
<link rel="stylesheet" href="https://fonts.googleapis.com/css2?family=PT+Sans:ital,wght@0,400;0,700;1,700&display=swap">
<style>
:root{
  --sky:#1fb3dc;
  --sky-light:#48d2f2;
  --sky-deep:#1288b0;
  --teal:#1a8aa6;
  --petrol:#15708a;
  --navy:#0b2233;
  --grey-bg:#e4e6e8;
  --grey-line:#b9c7cf;
  --grey-mark:#8a9299;
  --text:#1c1c1c;
  --white:#ffffff;
  --gold:#d4ad2c;
  --gold-dark:#a88517;
  --cta-blue:#3fc6ee;
  --btn-blue:#58a6cc;
}
*{box-sizing:border-box;margin:0;padding:0}
html,body{width:1200px;height:1162px;overflow:hidden}
body{position:relative;font-family:"PT Sans",Arial,sans-serif;color:var(--text);background:var(--grey-bg)}
.abs{position:absolute}
.top-band{left:0;top:0;width:1200px;height:394px;background:linear-gradient(135deg,var(--sky-deep) 0%,var(--sky) 35%,var(--sky-light) 55%,var(--sky) 80%,var(--sky-deep) 100%)}
.mid-band{left:0;top:394px;width:1200px;height:611px;background:linear-gradient(#dcdfe2,#eef0f1)}
.footer{left:0;top:1005px;width:1200px;height:157px;background:linear-gradient(var(--sky-deep),var(--sky) 60%,var(--sky-light))}
.recommend{left:837px;top:0;width:142px;height:21px;background:#d9eef5;font-size:9.5px;font-weight:700;color:var(--petrol);display:flex;align-items:center;justify-content:center;gap:4px}
.recommend span.plus{width:11px;height:11px;border:1.5px solid var(--petrol);border-radius:50%;font-size:9px;line-height:8px;text-align:center}
.brand{left:220px;top:34px;color:var(--white);font-size:34px;font-weight:700;letter-spacing:.3px;white-space:nowrap}
.brand small{font-size:26px}
.search{left:837px;top:64px;width:141px;height:22px;border-radius:6px;background:#2a7d98;border:1px solid #5fb6d0;color:var(--white);font-size:10px;padding-left:10px;display:flex;align-items:center}
.search svg{position:absolute;right:7px;top:4px}
.nav{left:221px;top:94px;width:758px;height:31px;background:linear-gradient(#19303e,var(--navy));border-radius:5px 5px 0 0;display:flex;align-items:center;font-size:12px;color:var(--white)}
.nav .home{width:40px;display:flex;justify-content:center}
.nav a{padding:0 13.5px;line-height:31px}
.nav a.active{background:#f2f3f4;color:var(--text);border-radius:4px 4px 0 0;height:25px;line-height:25px;margin-top:6px;padding:0 8px;position:relative}
.nav a.active::after{content:"";position:absolute;left:50%;bottom:-6px;margin-left:-6px;border:6px solid transparent;border-top-color:#f2f3f4;border-bottom:0}
.subnav{left:221px;top:125px;width:758px;height:25px;background:#f1f2f3;border-radius:0 0 4px 4px;font-size:11px;display:flex;align-items:center;gap:13px;padding-left:12px}
.hero{left:221px;top:154px;width:758px;height:256px;background:linear-gradient(90deg,#d9dfe3 0%,#e5eef3 35%,#bfe3f7 60%,#d3ecfa 100%);overflow:hidden}
.hero-people{left:0;top:0;width:330px;height:256px;background:linear-gradient(90deg,#cdb29e,#e4d6ca 70%,rgba(229,238,243,0))}
.hero-lift{right:0;top:0;width:170px;height:256px;background:linear-gradient(90deg,rgba(200,220,235,0),#c9d6df 50%,#b7c7d2)}
.hero h1{left:311px;top:66px;font-size:23px;color:var(--petrol);font-weight:700}
.hero h2{left:360px;top:96px;font-size:19px;color:var(--petrol);font-weight:700}
.hero p{left:362px;top:130px;font-size:12px;color:var(--petrol)}
.cta{left:688px;top:320px;width:300px;height:66px}
.cta span{position:absolute;right:70px;top:8px;text-align:right;color:var(--white);font-size:20px;font-weight:700;line-height:23px}
.aktion{left:51px;top:154px;width:143px;height:341px}
.aktion .title{position:absolute;left:0;top:6px;width:143px;text-align:center;color:var(--white);font-size:34px;font-weight:700}
.aktion .date{position:absolute;left:0;top:40px;width:143px;text-align:center;color:var(--white);font-size:11px}
.aktion .head{position:absolute;left:0;top:78px;width:143px;text-align:center;font-size:22px;line-height:25px;color:#17313d}
.aktion .lorem{position:absolute;left:12px;top:168px;width:120px;text-align:center;font-size:9px;line-height:13.5px;color:var(--white)}
.aktion .ribbon{position:absolute;left:-7px;top:243px;width:157px;height:33px;background:linear-gradient(#e6c341,var(--gold) 50%,var(--gold-dark));border-radius:3px;color:var(--white);font-size:11px;font-weight:700;text-align:center;line-height:29px}
.teaser{top:438px;width:243px;height:162px;overflow:hidden;background:#6e5a4c}
.teaser .photo{position:absolute;left:0;top:0;width:100%;height:106px}
.teaser .cap{position:absolute;left:0;top:106px;width:100%;height:56px;background:rgba(40,58,66,.9);padding:4px 8px;color:var(--white);font-size:9px;line-height:10.5px}
.teaser .cap b{color:#7fd7f5;display:block;font-size:9.5px}
.more{position:absolute;background:var(--cta-blue);color:var(--white);font-size:9.5px;font-weight:700;padding:1px 4px;white-space:nowrap}
.teaser .more{right:3px;bottom:2px}
.badge-new{left:478px;top:428px;width:50px;height:20px;background:linear-gradient(#3bc0ee,#1293c7);border:1.5px solid var(--white);border-radius:4px;color:var(--white);font-size:11px;font-weight:700;text-align:center;line-height:17px}
.call{left:736px;top:438px;width:243px;height:162px;background:var(--sky);padding:4px}
.call .inner{position:relative;width:100%;height:100%;background:linear-gradient(90deg,#2b9cc0,#5cc0df 55%,#cfe6ef)}
.call .agent{position:absolute;right:0;top:0;width:95px;height:154px;background:linear-gradient(90deg,rgba(230,240,245,0),#e9eef0)}
.call h3{position:absolute;left:11px;top:3px;color:var(--white);font-size:16px;font-weight:700}
.call .phone{position:absolute;left:10px;top:29px;color:var(--white);font-size:16px;font-weight:700;display:flex;align-items:center;gap:4px}
.call .free{position:absolute;left:37px;top:48px;font-size:6.5px;color:var(--white)}
.call .ask{position:absolute;left:11px;top:68px;color:var(--white);font-size:11.5px;font-weight:700;line-height:13.5px}
.call .field{position:absolute;top:105px;width:90px;height:17px;background:var(--white);font-size:7.5px;padding-left:8px;line-height:17px;color:var(--text)}
.call .send{position:absolute;left:11px;top:132px;width:119px;height:19px;background:var(--navy);border-radius:9px;color:var(--white);font-size:9.5px;font-weight:700;text-align:center;line-height:19px}
.rule{left:221px;width:758px;height:2px;background:var(--grey-line)}
.h-main{left:227px;top:645px;font-size:16px;font-weight:700}
.col{top:675px;width:357px;font-size:11.9px;line-height:13.5px;text-align:justify}
.mini{top:836px;width:352px;height:66px}
.mini .img{position:absolute;left:0;top:0;width:103px;height:66px;background:#33c9f2}
.mini h4{position:absolute;left:111px;top:-3px;font-size:12px}
.mini p{position:absolute;left:111px;top:13px;width:240px;font-size:9px;line-height:13.5px}
.partners-label{left:0;top:929px;width:1200px;text-align:center;font-size:11px;color:#666}
.partner{top:955px;width:112px;height:34px;display:flex;align-items:center;gap:6px}
.partner .dot{flex:none;width:20px;height:20px;background:var(--grey-mark);border-radius:50%}
.partner .name{font-size:20px;line-height:20px;color:#222}
.partner .tag{display:block;font-size:9px;line-height:11px;color:#222}
.to-top{left:1014px;top:782px;width:131px;height:22px;background:var(--teal);color:var(--white);font-size:12px;text-align:center;line-height:22px}
.to-top::before{content:"";position:absolute;left:38px;top:-23px;border:27px solid transparent;border-bottom:23px solid var(--teal);border-top:0}
.flinks{top:1027px;color:var(--white);font-size:11.5px;line-height:18px;text-transform:uppercase}
.social{left:916px;top:1030px;width:38px;height:38px;background:#3f67b0;border-radius:5px}
.copy{left:0;top:1123px;width:1200px;text-align:center;font-size:11.5px;color:var(--navy)}
</style>
</head>
<body>
<div class="abs top-band"></div>
<div class="abs mid-band"></div>

<div class="abs recommend"><span class="plus">+</span>Seite weiterempfehlen</div>
<div class="abs brand">Treppenlift <small>Infoportal</small></div>
<div class="abs search">Suchen...
  <svg width="14" height="14" viewBox="0 0 14 14"><circle cx="5.5" cy="5.5" r="4" fill="none" stroke="#fff" stroke-width="2"/><line x1="8.5" y1="8.5" x2="13" y2="13" stroke="#fff" stroke-width="2.5"/></svg>
</div>

<nav class="abs nav">
  <span class="home"><svg width="16" height="14" viewBox="0 0 16 14"><path d="M8 1 L15 7 H13 V13 H3 V7 H1 Z" fill="#fff"/></svg></span>
  <a class="active">Treppenlift</a>
  <a>Plattformlift</a><a>LifttypNr.3</a><a>LifttypNr.4</a><a>Fragen &amp; Antworten</a><a>Service</a><a>Partner</a><a>Kontakt</a>
</nav>
<div class="abs subnav">Kurvige Treppen: <b>Lifttyp1</b> Gerade Treppen: <b>Lifttyp2</b> Treppen Außen: <b>Lifttyp3</b></div>

<section class="abs hero">
  <div class="abs hero-people" role="img" aria-label="Foto eines lächelnden älteren Paares"></div>
  <div class="abs hero-lift" role="img" aria-label="Foto eines Treppenlift-Sitzes"></div>
  <h1 class="abs">Welcher Treppenlift</h1>
  <h2 class="abs">passt am besten zu Ihnen?</h2>
  <p class="abs">Jetzt kostenlos Angebote anfordern</p>
</section>
<div class="abs cta">
  <svg width="300" height="66" viewBox="0 0 300 66"><path d="M20 0 H290 V66 H20 L0 33 Z" fill="#d4ad2c"/><path d="M20 0 H290 V33 H0 Z" fill="#e4c447"/><path d="M255 16 L266 33 L255 50" fill="none" stroke="#fff" stroke-width="5"/></svg>
  <span>Kostenlos Angebote<br>anfordern</span>
</div>

<aside class="abs aktion">
  <svg class="abs" width="143" height="341" viewBox="0 0 143 341" style="left:0;top:0"><defs><linearGradient id="ak" x1="0" y1="0" x2="0" y2="1"><stop offset="0" stop-color="#7fc4d8"/><stop offset=".5" stop-color="#5aa7c0"/><stop offset="1" stop-color="#2d7e9b"/></linearGradient></defs><path d="M0 4 Q0 0 4 0 H139 Q143 0 143 4 V300 L71 341 L0 300 Z" fill="url(#ak)"/></svg>
  <div class="title">AKTION</div>
  <div class="date">VOM 03.10 - 21.12.2012</div>
  <div class="head">HEADLINE<br>MUSTER<br>BEISPIEL</div>
  <div class="lorem">Lorem ipsum dolor sit amet, consetetur sadipscing elitr, sed diam nonumy eirmod tempor invidunt ut labore et dolore magna aliquyam</div>
  <div class="ribbon">JETZT INFORMIEREN</div>
</aside>

<article class="abs teaser" style="left:221px">
  <div class="photo" role="img" aria-label="Foto eines Plattformlifts an einer Treppe" style="background:linear-gradient(135deg,#e8c98c,#8a2b2b 55%,#c9b8a4)"></div>
  <div class="cap"><b>Plattformlift - Muster Slogan</b>Lorem ipsum dolor sit amet, consetetur sadipscing elitr, sed diam nonumy eirmod tempor invidunt ut labore et dolore magna aliquyam</div>
  <span class="more">Erfahren Sie mehr</span>
</article>
<article class="abs teaser" style="left:478px">
  <div class="photo" role="img" aria-label="Foto eines Sitzlifts an einer Treppe" style="background:linear-gradient(135deg,#efe2c0,#c9a66a 55%,#8c6a3e)"></div>
  <div class="cap"><b>Sitzlift - Sicherheit &amp; Komfort</b>Lorem ipsum dolor sit amet, consetetur sadipscing elitr, sed diam nonumy eirmod tempor invidunt ut labore et dolore magna aliquyam</div>
  <span class="more">Erfahren Sie mehr</span>
</article>
<div class="abs badge-new">NEU!</div>

<section class="abs call">
  <div class="inner">
    <div class="agent" role="img" aria-label="Foto einer Beraterin mit Headset"></div>
    <h3>Beratungs Telefon</h3>
    <div class="phone"><svg width="22" height="22" viewBox="0 0 22 22"><circle cx="11" cy="11" r="10" fill="none" stroke="#fff" stroke-width="1.5"/><path d="M5 9 Q11 5 17 9 V11 H14 V9.5 H8 V11 H5 Z M7 12 H15 L16 16 H6 Z" fill="#fff"/></svg>0800 31 52 9</div>
    <div class="free">gebührenfrei</div>
    <div class="ask">Fordern Sie jetzt<br>unseren Rückruf an</div>
    <div class="field" style="left:11px">Ihr Name</div>
    <div class="field" style="left:105px">Ihre Telefonnummer</div>
    <div class="send">Rückruf anfordern!</div>
  </div>
</section>

<div class="abs rule" style="top:627px"></div>
<h2 class="abs h-main">Headline 1</h2>
<p class="abs col" style="left:227px">Lorem ipsum dolor sit amet, consetetur sadipscing elitr, sed diam nonumy eirmod tempor invidunt ut labore et dolore magna aliquyam erat, sed diam voluptua. At vero eos et accusam et justo duo dolores et ea rebum. Stet clita kasd gubergren, no sea takimata sanctus est Lorem ipsum dolor sit amet. Lorem ipsum dolor sit amet, consetetur sadipscing elitr, sed diam nonumy eirmod tempor invidunt ut labore et dolore magna aliquyam erat, sed diam voluptua. At vero eos et accusam et justo duo dolores et ea rebum. Stet clita kasd gubergren, no sea takimata sanctus est Lorem ipsum dolor sit amet.</p>
<p class="abs col" style="left:614px">Lorem ipsum dolor sit amet, consetetur sadipscing elitr, sed diam nonumy eirmod tempor invidunt ut labore et dolore magna aliquyam erat, sed diam voluptua. At vero eos et accusam et justo duo dolores et ea rebum. Stet clita kasd gubergren, no sea takimata sanctus est Lorem ipsum dolor sit amet. Lorem ipsum dolor sit amet, consetetur sadipscing elitr, sed diam nonumy eirmod tempor invidunt ut labore et dolore magna aliquyam erat, sed diam voluptua. At vero eos et accusam et justo duo dolores et ea rebum. Stet clita kasd gubergren, no sea takimata sanctus est Lorem ipsum dolor sit amet.</p>
<span class="abs more" style="left:887px;top:808px;background:var(--btn-blue)">Erfahren Sie mehr</span>
<div class="abs rule" style="top:825px"></div>

<article class="abs mini" style="left:221px">
  <div class="img" role="img" aria-label="Platzhalterbild"></div>
  <h4>Headline</h4>
  <p>Lorem ipsum dolor sit amet, consetetur sadipscing elitr, sed diam nonumy eirmod tempor invidunt ut labore et dolore magna aliquyam aliquyam.</p>
  <span class="more" style="background:var(--btn-blue);right:-2px;bottom:-4px">Erfahren Sie mehr</span>
</article>
<article class="abs mini" style="left:614px;top:838px">
  <div class="img" role="img" aria-label="Platzhalterbild"></div>
  <h4>Headline</h4>
  <p>Lorem ipsum dolor sit amet, consetetur sadipscing elitr, sed diam nonumy eirmod tempor invidunt ut labore et dolore magna aliquyam aliquyam.</p>
  <span class="more" style="background:var(--btn-blue);right:-8px;bottom:-4px">Erfahren Sie mehr</span>
</article>
<div class="abs rule" style="top:910px"></div>

<div class="abs partners-label">Unsere Partner :</div>
<svg class="abs" style="left:220px;top:956px" width="24" height="30" viewBox="0 0 24 30"><path d="M20 2 L6 15 L20 28" fill="none" stroke="#8a9299" stroke-width="6"/></svg>
<svg class="abs" style="left:956px;top:956px" width="24" height="30" viewBox="0 0 24 30"><path d="M4 2 L18 15 L4 28" fill="none" stroke="#8a9299" stroke-width="6"/></svg>
<div class="abs partner" style="left:252px"><span class="dot"></span><span class="name">Carenta<span class="tag">Pflege &amp; Hilfe</span></span></div>
<div class="abs partner" style="left:400px"><span class="dot"></span><span class="name">Carenta<span class="tag">Pflege &amp; Hilfe</span></span></div>
<div class="abs partner" style="left:549px"><span class="dot"></span><span class="name">Carenta<span class="tag">Pflege &amp; Hilfe</span></span></div>
<div class="abs partner" style="left:697px"><span class="dot"></span><span class="name">Carenta<span class="tag">Pflege &amp; Hilfe</span></span></div>
<div class="abs partner" style="left:838px"><span class="dot"></span><span class="name">Carenta<span class="tag">Pflege &amp; Hilfe</span></span></div>

<div class="abs to-top">Zum Seitenanfang</div>

<footer class="abs footer"></footer>
<div class="abs flinks" style="left:237px">Unternehmen<br>Service<br>Partner<br>Fragen &amp; Antworten</div>
<div class="abs flinks" style="left:412px">Treppenlift<br>Plattformlift<br>Lifttyp 1<br>Lifttyp 2</div>
<div class="abs flinks" style="left:535px">Impressum<br>Kontakt<br>Nutzungsbedingungen</div>
<div class="abs social" aria-label="Soziales Netzwerk"></div>
<div class="abs copy">© 2012 UNTERNEHMEN, Musterstraße 46, 45676 Musterstadt</div>
</body>
</html>
```